Free Charity Events from KOVAPLAY

The purpose of the landing page is to get all visitors excited about playing in our Free $500 Charity Tournaments. The visitors who click on the landing page will receive 3 free entries into 3 different $500 Charity Tournaments. A $500 Blackjack Tournament, a $500 Texas Holdem Tournament, and a $500 Baccarat Tournament.

We also offer Free Qualifying games 24/7, where players can earn additional entries into our real paying tournaments.

We will reward the winners in each tournament with a share of the $500 and we will reward a worthy cause or charity with $500 as well.

The money comes from advertising shown during the qualifying game.

Our website is currently being developed on our teams development server. Here is a private link to the site. https://dev.kovaplay.net Attached are vector images of our logo.

Also attached are two attempts we made at a landing page.

Target Market(s)

Social Game Players

Industry/Entity Type

Games

Contact Information for Business Card

The purpose of the business card will be to promote our Free Charity Games. There will be a code hand written on the card. (Meaning we will need a white box to write the code in) If the holder of the card enters that code during registration, they will receive 3 free entries into our real cash tournaments. The giver of the card will receive the affiliate bonus for referring a new player.

Font styles to use
Serif
Sans Serif

Colors
9bcb3c
0292cd
ec1f27

Requirements
Must have
• Excitement, i also like humor but that isn't a must, excitement is.
Nice to have
• Humor
Should not have
• Too many words, we are looking for that image that says at least a few hundred words.

```html
<!DOCTYPE html>
<html lang="en">
<head>
<meta charset="utf-8">
<title>KOVAPLAY – Free $500 Charity Tournaments</title>
<link rel="stylesheet" href="https://fonts.googleapis.com/css2?family=Oswald:wght@400;500&family=Open+Sans:wght@400;700&family=Lobster&display=swap">
<style>
  :root {
    --ink: #000000;
    --paper: #ffffff;
    --red: #d0112b;
    --green: #86a94a;
    --blue: #3a72b0;
    --photo-dark: #1a1a1c;
    --photo-felt: #159b86;
  }
  * { margin: 0; padding: 0; box-sizing: border-box; }
  html, body { width: 1200px; height: 1106px; overflow: hidden; background: var(--ink); }
  .landing {
    position: relative;
    width: 1200px;
    height: 1106px;
    background: var(--ink);
    color: var(--paper);
    font-family: "Open Sans", Arial, sans-serif;
    overflow: hidden;
  }
  .hero-art { position: absolute; inset: 0; }
  .brand {
    position: absolute; left: 90px; top: 48px;
    display: flex; align-items: center; gap: 16px;
  }
  .brand-dot { width: 80px; height: 80px; border-radius: 50%; background: var(--green); }
  .brand-name {
    font-family: "Oswald", sans-serif; font-weight: 500;
    font-size: 76px; line-height: 1; color: var(--green); letter-spacing: 1px;
  }
  .headline {
    position: absolute; left: 92px; top: 160px;
    font-family: "Oswald", sans-serif; font-weight: 400;
    font-size: 102px; line-height: 1; letter-spacing: -1px;
  }
  .subhead {
    position: absolute; left: 94px; top: 258px;
    font-family: "Oswald", sans-serif; font-weight: 400;
    font-size: 40px; line-height: 1;
  }
  .games { position: absolute; left: 0; top: 353px; width: 700px; }
  .game {
    position: absolute; top: 0; width: 200px; margin-left: -100px;
    text-align: center;
  }
  .game-badge {
    width: 132px; height: 132px; border-radius: 50%;
    margin: 0 auto; display: flex; align-items: center; justify-content: center;
  }
  .game-badge svg { width: 76px; height: 76px; }
  .badge-holdem { background: var(--red); }
  .badge-blackjack { background: var(--green); }
  .badge-baccarat { background: var(--blue); }
  .game-name {
    margin-top: 22px;
    font-family: "Lobster", cursive; font-size: 22px; line-height: 27px;
  }
  .offer-title {
    position: absolute; left: 92px; top: 630px;
    font-weight: 700; font-size: 43px; line-height: 54px;
  }
  .offer-text {
    position: absolute; left: 90px; top: 762px;
    font-size: 23px; line-height: 37px;
  }
  .reward-text {
    position: absolute; left: 90px; top: 854px;
    font-size: 22.5px; line-height: 38px;
  }
  .cta {
    position: absolute; left: 90px; top: 980px;
    width: 307px; height: 64px;
    border: 2px solid var(--paper); border-radius: 4px;
    display: flex; align-items: center; justify-content: center;
    font-size: 27px; color: var(--paper); text-decoration: none; letter-spacing: 0.3px;
  }
</style>
</head>
<body>
<main class="landing">
  <svg class="hero-art" width="1200" height="1106" viewBox="0 0 1200 1106">
    <defs>
      <linearGradient id="tableTone" x1="0" y1="0" x2="0" y2="1">
        <stop offset="0" stop-color="var(--photo-dark)"/>
        <stop offset="0.3" stop-color="#2a2526"/>
        <stop offset="0.55" stop-color="#1f6f63"/>
        <stop offset="1" stop-color="var(--photo-felt)"/>
      </linearGradient>
    </defs>
    <polygon role="img" aria-label="Photo of a hand lifting a playing card beside stacks of casino chips on a green felt table"
             points="548,0 1200,0 1200,1106 954,1106" fill="url(#tableTone)"/>
    <polygon class="divider" points="528,0 548,0 954,1106 936,1106" fill="var(--red)"/>
  </svg>

  <header class="brand">
    <span class="brand-dot"></span>
    <span class="brand-name">KOVAPLAY</span>
  </header>

  <h1 class="headline">Free $500</h1>
  <h2 class="subhead">Charity Tournaments</h2>

  <section class="games">
    <div class="game" style="left:190px">
      <div class="game-badge badge-holdem">
        <svg viewBox="0 0 76 76" fill="none" stroke="#fff" stroke-width="3" stroke-linejoin="round">
          <rect x="30" y="8" width="26" height="36" rx="3" transform="rotate(15 43 26)"/>
          <rect x="18" y="14" width="26" height="36" rx="3" transform="rotate(-5 31 32)"/>
          <rect x="8" y="28" width="26" height="36" rx="3" transform="rotate(-20 21 46)"/>
          <circle cx="60" cy="60" r="8"/>
        </svg>
      </div>
      <p class="game-name">Texas Hold'em<br>Tournament</p>
    </div>
    <div class="game" style="left:380px">
      <div class="game-badge badge-blackjack">
        <svg viewBox="0 0 76 76" fill="none" stroke="#fff" stroke-width="3" stroke-linejoin="round">
          <rect x="40" y="6" width="26" height="40" rx="2"/>
          <rect x="26" y="16" width="26" height="40" rx="2"/>
          <rect x="10" y="26" width="26" height="42" rx="2"/>
          <path d="M23 36 L29 47 L23 58 L17 47 Z"/>
        </svg>
      </div>
      <p class="game-name">Blackjack<br>Tournament</p>
    </div>
    <div class="game" style="left:569px">
      <div class="game-badge badge-baccarat">
        <svg viewBox="0 0 76 76" fill="none" stroke="#fff" stroke-width="3" stroke-linejoin="round" stroke-linecap="round">
          <rect x="42" y="4" width="26" height="36" rx="2"/>
          <path d="M48 28 L36 40 L42 46 L54 34"/>
          <path d="M38 44 L10 68"/>
          <circle cx="9" cy="69" r="4"/>
        </svg>
      </div>
      <p class="game-name">Baccarat<br>Tournament</p>
    </div>
  </section>

  <h3 class="offer-title">Offer Free Qualifying<br>Games 24/7</h3>
  <p class="offer-text">Where Players Can Earn Additional Entries<br>Into Our&nbsp; Real Paying Tournaments.</p>
  <p class="reward-text">We will reward the winners in each tournament with a share of the<br>$500 and we will reward a worthy cause or charity with $500 as well.</p>

  <a class="cta" href="https://dev.kovaplay.net">ONLINE GAMES</a>
</main>
</body>
</html>
```